Car rental website design for a UAE car rental company

This project is about creating a new website design for a car rental company located in Dubai (United Arab Emirates), I opened the same project a few months ago but I didn't receive a lot of appealing entries so I closed it but this time I am marking the project as guaranteed to avoid such situation again, if you have already provided a design before then please re-submit again on this project so that it is considered while reviewing all the designs

A few important things:

1- We need a simple non-complex design
2- The final deliverable would be 2 screens (PSD, JPEG ... etc), the first screen is for the home page and the second screen is for an internal page
3- The home page must have a section that end users can use to rent a car online directly from the home page instead of going into some inner pages
4- The current website is very old and not very appealing so avoid creating a similar design (www.quarvin-drive.example)
5- The name is Quarvin but the company rents normal cars (no Limousin cars will be rented) so avoid adding any fancy cars in the images/graphics used in the design, just normal end users cars
6- The expected pages would be: home, About us, Our team, Strategy, Contact us and links to social media pages
7- The attachments include the company's logo and some screens from other car rental companies that provide online rentals/payments

If you have any questions please feel free to ask and please note that we will need the designs urgently

Thanks

Target Market(s)

Dubai - United Arab Emirates

Industry/Entity Type

It Company

Number of Pages Required

2 page

Font styles to use
Sans Serif

Requirements
Must have
• Check the project details
Nice to have
Should not have

```html
<!DOCTYPE html>
<html lang="en">
<head>
<meta charset="utf-8">
<title>Quarvin Rent A Car</title>
<link href="https://fonts.googleapis.com/css2?family=Montserrat:wght@400;500;600;700;800&display=swap" rel="stylesheet">
<style>
:root{
  --brand:#a5133c;
  --dark:#1f2a30;
  --nav-line:#38444b;
  --ink:#222;
  --yellow:#f6d21b;
  --panel:#fbf2f4;
  --line:#e2c4cc;
  --white:#fff;
  --hero-top:#9fb3ab;
  --hero-mid:#5f8a45;
  --hero-low:#4a6a3a;
  --hero-road:#8d9590;
}
*{box-sizing:border-box;margin:0;padding:0}
html,body{width:1200px;height:900px;overflow:hidden;background:var(--white);font-family:'Montserrat',sans-serif;color:var(--ink)}
.canvas{position:relative;width:1200px;height:900px}

.hero-photo{position:absolute;left:0;top:0;width:1200px;height:545px;
  background:linear-gradient(180deg,var(--hero-top) 0%,var(--hero-mid) 35%,var(--hero-low) 65%,var(--hero-road) 100%)}

.header{position:absolute;left:172px;top:0;width:856px;height:86px}
.brand{position:absolute;left:0;top:0;width:120px;height:86px;background:var(--white);display:flex;flex-direction:column;align-items:center;justify-content:center;gap:6px}
.brand-mark{width:30px;height:30px;background:var(--brand)}
.brand-name{font-size:15px;font-weight:600;color:var(--brand)}
.topbar{position:absolute;left:120px;top:0;width:736px;height:40px;background:var(--white);font-size:13px;display:flex;align-items:center}
.topbar .book{color:var(--brand);font-weight:500;margin-left:1px}
.topbar .phone{margin-left:14px;font-weight:500}
.social{position:absolute;left:332px;top:10px;display:flex;gap:10px}
.social span{width:20px;height:20px;border-radius:50%;background:#111;display:block}
.login{position:absolute;left:590px;font-weight:500}
.join{position:absolute;right:0;top:0;width:83px;height:40px;background:var(--brand);color:var(--white);font-weight:600;display:flex;align-items:center;justify-content:center}

.nav{position:absolute;left:120px;top:40px;width:736px;height:46px;background:var(--dark);display:flex}
.nav .home{width:36px;height:46px;background:var(--brand);display:flex;align-items:center;justify-content:center}
.nav a{color:var(--white);text-decoration:none;font-size:13.5px;font-weight:500;height:46px;display:flex;align-items:center;justify-content:center;border-left:1px solid var(--nav-line);white-space:nowrap}
.nav a:first-of-type{border-left:0}

.price{position:absolute;left:607px;top:233px;width:113px;height:43px;background:var(--yellow);display:flex;align-items:center;padding-left:6px;color:var(--brand);font-weight:800}
.price small{font-size:9px;font-weight:700;color:#333}
.price b{font-size:30px;margin:0 3px}
.price::after{content:"";position:absolute;left:4px;bottom:-7px;border:7px solid transparent;border-top-color:var(--yellow);border-bottom:0}

.tagline-1{position:absolute;left:418px;top:378px;height:28px;background:var(--white);padding:0 10px;font-size:24px;font-weight:700;line-height:28px;white-space:nowrap}
.tagline-2{position:absolute;left:295px;top:408px;height:28px;background:var(--white);padding:0 11px;font-size:25.5px;font-weight:400;line-height:28px;white-space:nowrap}

.booking{position:absolute;left:172px;top:471px;width:856px;height:164px}
.tabs{height:33px;background:var(--white);border:1px solid var(--line);border-bottom:0;display:flex;font-size:13.5px;color:var(--brand);font-weight:500}
.tabs span{display:flex;align-items:center;justify-content:center}
.tabs .active{background:var(--brand);color:var(--white);font-weight:600}
.form{height:131px;background:var(--panel);border:1px solid var(--line);position:relative}
.label{position:absolute;top:14px;font-size:13px;font-weight:600}
.label small{font-weight:400;font-size:12px;color:#555}
.field{position:absolute;top:40px;height:34px;background:var(--white);border:1px solid var(--line);font-size:13.5px;display:flex;align-items:center;padding-left:8px}
.field.date{flex-direction:column;align-items:flex-start;justify-content:center;font-size:12.5px;line-height:13px}
.field.date .d{color:var(--brand)}
.cal{position:absolute;right:6px;top:6px;width:22px;height:21px;border:1.5px solid #999;border-radius:3px}
.help{position:absolute;left:290px;top:44px;width:27px;height:27px;border-radius:50%;background:var(--brand);color:var(--white);font-weight:700;display:flex;align-items:center;justify-content:center;font-size:14px}
.coupon{color:#aaa}
.coupon em{position:absolute;right:10px;color:var(--brand);font-style:normal;font-weight:500;font-size:14px}
.divider{position:absolute;left:0;right:0;top:87px;border-top:1px solid var(--line)}
.return{position:absolute;left:12px;top:98px;font-size:13.5px;display:flex;align-items:center;gap:6px}
.return i{width:17px;height:17px;border:2.5px solid var(--brand);border-radius:50%}
.quote{position:absolute;right:9px;top:93px;width:111px;height:32px;background:var(--brand);color:var(--white);font-weight:600;font-size:13.5px;display:flex;align-items:center;justify-content:center}

.promo{position:absolute;left:172px;top:673px;width:856px;height:227px;
  background:linear-gradient(160deg,#a9b4a8 0%,#557a4a 35%,#3d5a3a 60%,#6d7a80 100%)}
.promo-brand{position:absolute;right:26px;top:16px;color:var(--white);text-align:center;font-weight:800;font-size:22px;line-height:20px}
.promo-brand small{display:block;font-size:8px;font-weight:600;letter-spacing:1px}
.promo-text{position:absolute;left:27px;top:140px;color:var(--white);font-weight:700;text-transform:uppercase}
.promo-text .l1{font-size:21px}
.promo-text .l2{font-size:27px;line-height:30px}
.promo-text .l3{font-size:20px}
</style>
</head>
<body>
<div class="canvas">
  <div class="hero-photo" role="img" aria-label="Photo of a black family sedan parked on a country road beside a red barn and dark wooden fences"></div>

  <header class="header">
    <div class="brand"><span class="brand-mark"></span><span class="brand-name">Quarvin</span></div>
    <div class="topbar">
      <span class="book">BOOK A CAR</span>
      <span class="phone">+97 140 000 123</span>
      <div class="social"><span></span><span></span><span></span><span></span></div>
      <span class="login">LOGIN</span>
      <span class="join">JOIN NOW</span>
    </div>
    <nav class="nav">
      <span class="home"><svg width="20" height="18" viewBox="0 0 20 18" fill="none" stroke="#fff" stroke-width="1.6"><path d="M2 9 10 2l8 7M4 8v9h4v-5h4v5h4V8"/></svg></span>
      <a style="width:124px">RESERVATIONS</a><a style="width:78px">LEASING</a><a style="width:60px">RENT</a><a style="width:73px">OFFERS</a><a style="width:95px">ABOUT US</a><a style="width:97px">OUR TEAM</a><a style="width:87px">STRATEGY</a><a style="width:86px">CONTACT</a>
    </nav>
  </header>

  <div class="price"><small>AED</small><b>120</b><small>DAY</small></div>
  <div class="tagline-1">EXPERAINCE AN EXTRA MILE</div>
  <div class="tagline-2">of comfort, pleasure and leisure from the best</div>

  <section class="booking">
    <div class="tabs">
      <span style="width:92px">COUPE</span><span style="width:80px">SEDAN</span><span style="width:80px">SUV</span><span style="width:64px">WAGON</span>
      <span style="width:52px"></span><span class="active" style="width:117px">SPORTS CAR</span><span style="width:136px">CONVERTIBLE</span><span style="width:118px">LUXURY CAR</span><span style="width:117px">ROSSOVER</span>
    </div>
    <div class="form">
      <span class="label" style="left:8px">Pick-up-Location <small>(City, State or Airport code)</small></span>
      <div class="field" style="left:9px;width:272px">at&nbsp;<b>Dubai Airport,</b>&nbsp;8TH GATE</div>
      <span class="help">?</span>
      <span class="label" style="left:324px">Pick-up Date/Time</span>
      <div class="field date" style="left:324px;width:144px"><span class="d">March 25 2015</span><span>10:30AM</span><i class="cal"></i></div>
      <span class="label" style="left:489px">Return Date/Time</span>
      <div class="field date" style="left:490px;width:144px"><span class="d">April 15 2015</span><span>10:30AM</span><i class="cal"></i></div>
      <span class="label" style="left:666px">Apply A Coupon Code</span>
      <div class="field coupon" style="left:666px;width:181px;padding-left:11px">AYRN41689<em>APPLY</em></div>
      <div class="divider"></div>
      <label class="return"><i></i>Return car to a different location</label>
      <span class="quote">GET A QUOTE</span>
    </div>
  </section>

  <section class="promo" role="img" aria-label="Photo of a winding mountain road through a green forested valley">
    <div class="promo-brand">ROVEN<small>DRIVE YOURSELF</small></div>
    <div class="promo-text"><div class="l1">Choose from over</div><div class="l2">33 car models</div><div class="l3">and drive yourself.</div></div>
  </section>
</div>
</body>
</html>
```